Business Card Design Project

I need a new business card for side business. Very simple and to the point. I am a licensed massage therapist and want the colors to be warm. I don't have a logo or company name. I just need to convey that I am a Licensed Massage Therapist and have my contact information so people can contact me. I'll attach some files that I like. I am a male so I don't want it to be feminine.

One file is my existing card. I like Tamsin's card and the layout so would prefer a similar layout. I would like to incorporate my swimmer/biker/runner image. Doesn't have to be the exact likeness because I don't have that file but something similar to that. I would like to also include my areas of specialty of: Swedish, Deep Tissue, Sports, and Hot Stone

I would also like to incorporate a QR code on the back of the card centered.
Updates

Payment is NOW guaranteed to the design I choose.  I updated my creative brief so hopefully it is more clear.  

Industry/Entity Type

Massage

Requirements
Must have
• Gavin Thrushwell
Licensed Massage Therapist
or
Massage Therapy
203-555-0187
gthrushwell@mailvale.net

```html
<!DOCTYPE html>
<html lang="en">
<head>
<meta charset="utf-8">
<title>Gavin Thrushwell – Massage Therapy Business Card</title>
<link rel="stylesheet" href="https://fonts.googleapis.com/css2?family=Quicksand:wght@400;500&display=swap">
<style>
  :root {
    --backdrop: #3a3a3a;
    --card-paper: #f4f3f0;
    --ink-gold: #8f6a22;
    --band-gold: #98731f;
    --band-text: #f7f2e6;
    --icon-tint: #e3d6b8;
  }
  * { box-sizing: border-box; margin: 0; padding: 0; }
  html, body {
    width: 1200px;
    height: 1006px;
    overflow: hidden;
    background: var(--backdrop);
    font-family: "Quicksand", sans-serif;
  }
  .business-card {
    position: absolute;
    left: 150px;
    top: 246px;
    width: 900px;
    height: 514px;
    background: var(--card-paper);
    color: var(--ink-gold);
  }
  .sport-icons {
    position: absolute;
    left: 60px;
    top: 150px;
    width: 370px;
    height: 100px;
    background: linear-gradient(90deg, var(--icon-tint), #efe6d2);
    border-radius: 6px;
  }
  .service-title {
    position: absolute;
    left: 60px;
    top: 264px;
    font-size: 43px;
    font-weight: 500;
    letter-spacing: 0.3px;
    white-space: nowrap;
    line-height: 1.2;
  }
  .dotted-divider {
    position: absolute;
    left: 474px;
    top: 112px;
    width: 10px;
    height: 230px;
  }
  .contact-block {
    position: absolute;
    left: 512px;
    top: 104px;
    white-space: nowrap;
  }
  .therapist-name {
    font-size: 36px;
    font-weight: 500;
    line-height: 1.1;
  }
  .therapist-title {
    font-size: 22px;
    font-weight: 500;
    margin-top: 4px;
  }
  .contact-lines {
    list-style: none;
    margin-top: 40px;
    font-size: 24px;
    font-weight: 500;
    line-height: 1.4;
  }
  .contact-label { margin-right: 10px; }
  .specialty-band {
    position: absolute;
    left: 0;
    top: 400px;
    width: 100%;
    height: 64px;
    background: var(--band-gold);
    color: var(--band-text);
    display: flex;
    align-items: center;
    justify-content: center;
    font-size: 27px;
    font-weight: 500;
    letter-spacing: 0.5px;
  }
</style>
</head>
<body>
  <section class="business-card">
    <div class="sport-icons" role="img" aria-label="Line icons of a swimmer, a cyclist and a runner"></div>
    <h1 class="service-title">Massage Therapy</h1>

    <svg class="dotted-divider" viewBox="0 0 10 230" aria-hidden="true">
      <g fill="var(--ink-gold)">
        <circle cx="5" cy="5" r="4.5"/>
        <circle cx="5" cy="36" r="4.5"/>
        <circle cx="5" cy="67" r="4.5"/>
        <circle cx="5" cy="98" r="4.5"/>
        <circle cx="5" cy="129" r="4.5"/>
        <circle cx="5" cy="160" r="4.5"/>
        <circle cx="5" cy="191" r="4.5"/>
        <circle cx="5" cy="222" r="4.5"/>
      </g>
    </svg>

    <div class="contact-block">
      <h2 class="therapist-name">Gavin Thrushwell</h2>
      <p class="therapist-title">Licensed Massage Therapist</p>
      <ul class="contact-lines">
        <li><span class="contact-label">t:</span>203-555-0187</li>
        <li><span class="contact-label">e:</span>gthrushwell@mailvale.net</li>
      </ul>
    </div>

    <div class="specialty-band">Swedish • Deep Tissue • Sports • Hot Stone</div>
  </section>
</body>
</html>
```